Corvane Supplies Business Card

Professional business card that stand out to our potential customers. Front and back with clean modern design

Industry/Entity Type

Oil and gas

Contact Information for Business Card

Name, address, website , office phone and cell number

Requirements
Must have
• Editable files for each employee

```html
<!DOCTYPE html>
<html lang="en">
<head>
<meta charset="utf-8">
<title>Corvane Supplies Business Card</title>
<link href="https://fonts.googleapis.com/css2?family=Roboto:wght@400;500;700&display=swap" rel="stylesheet">
<style>
  :root {
    --backdrop: #3b3b3d;
    --card: #ffffff;
    --brand-red: #e8141b;
    --brand-cyan: #1aaed0;
    --ink: #1e1e1e;
    --rule: #9a9a9a;
  }
  * { box-sizing: border-box; margin: 0; padding: 0; }
  html, body { width: 1200px; height: 694px; overflow: hidden; }
  body {
    background: var(--backdrop);
    font-family: "Roboto", Arial, sans-serif;
    position: relative;
  }
  .card {
    position: absolute;
    top: 192px;
    width: 540px;
    height: 310px;
    background: var(--card);
    border-radius: 34px;
  }
  .card--front { left: 40px; }
  .card--back { left: 620px; }

  .wordmark {
    display: flex;
    align-items: center;
    gap: 10px;
    color: var(--brand-red);
    font-weight: 700;
    text-transform: uppercase;
    letter-spacing: 1px;
    white-space: nowrap;
  }
  .wordmark__square {
    background: var(--brand-red);
    flex: none;
  }
  .card--front .wordmark {
    position: absolute;
    left: 50%; top: 50%;
    transform: translate(-50%, -50%);
    font-size: 34px;
  }
  .card--front .wordmark__square { width: 30px; height: 30px; }

  .card--back .wordmark {
    position: absolute;
    left: 30px; top: 138px;
    font-size: 17px;
    gap: 7px;
  }
  .card--back .wordmark__square { width: 16px; height: 16px; }

  .divider {
    position: absolute;
    left: 232px; top: 36px; bottom: 36px;
    width: 1px;
    background: var(--rule);
  }
  .contact {
    position: absolute;
    left: 256px; top: 40px; right: 24px;
  }
  .contact__name {
    font-size: 26px;
    font-weight: 400;
    color: var(--ink);
    line-height: 1.1;
  }
  .contact__role {
    font-size: 14px;
    font-weight: 500;
    color: var(--brand-red);
    margin-top: 2px;
  }
  .contact__address {
    font-size: 13.5px;
    color: var(--brand-cyan);
    line-height: 1.3;
    margin-top: 12px;
  }
  .contact__list {
    list-style: none;
    margin-top: 10px;
  }
  .contact__item {
    display: flex;
    align-items: flex-start;
    gap: 10px;
    font-size: 13.5px;
    color: var(--ink);
    line-height: 1.3;
    margin-bottom: 7px;
  }
  .contact__icon {
    width: 15px; height: 15px;
    flex: none;
    margin-top: 1px;
    fill: var(--brand-red);
  }
</style>
</head>
<body>

  <section class="card card--front" aria-label="Card front">
    <div class="wordmark">
      <span class="wordmark__square"></span>
      <span class="wordmark__name">Corvane Supplies</span>
    </div>
  </section>

  <section class="card card--back" aria-label="Card back">
    <div class="wordmark">
      <span class="wordmark__square"></span>
      <span class="wordmark__name">Corvane Supplies</span>
    </div>

    <div class="divider"></div>

    <div class="contact">
      <h1 class="contact__name">Dale Whitcombe</h1>
      <p class="contact__role">Owner</p>
      <p class="contact__address">412 N Ridgeline Ave Suite 5,<br>Midland, TX 79705, United States</p>
      <ul class="contact__list">
        <li class="contact__item">
          <svg class="contact__icon" viewBox="0 0 16 16" aria-hidden="true"><path d="M2 5c0-2 2-3 6-3s6 1 6 3v1h-3V5H5v1H2z"/><path d="M4 8h8l2 5H2z"/></svg>
          <span>(555)214-0387</span>
        </li>
        <li class="contact__item">
          <svg class="contact__icon" viewBox="0 0 16 16" aria-hidden="true"><path d="M1 3h14v10H1z"/><path d="M1 3l7 6 7-6" fill="none" stroke="#fff" stroke-width="1.4"/></svg>
          <span>sales@corvanesupplies.com</span>
        </li>
        <li class="contact__item">
          <svg class="contact__icon" viewBox="0 0 16 16" aria-hidden="true"><circle cx="8" cy="8" r="7"/><path d="M1 8h14M8 1c3 3 3 11 0 14M8 1c-3 3-3 11 0 14" fill="none" stroke="#fff" stroke-width="1"/></svg>
          <span>www.corvanesupplies.com</span>
        </li>
        <li class="contact__item">
          <svg class="contact__icon" viewBox="0 0 16 16" aria-hidden="true"><circle cx="8" cy="9" r="6" fill="none" stroke="#e8141b" stroke-width="1.6"/><path d="M8 6v3.5l2 1.5" fill="none" stroke="#e8141b" stroke-width="1.4"/><path d="M1 4l3-3M15 4l-3-3" stroke="#e8141b" stroke-width="1.6"/></svg>
          <span>Monday – Friday<br>8:30am – 5pm</span>
        </li>
      </ul>
    </div>
  </section>

</body>
</html>
```